Landing Page for Social Media Optimization

We need a Landing page made for Social Media Optimization we are going to be calling this Trevinoxa an entire package that is for small to large businesses. We will manage all aspects of social media from Plimvera, Quondel Marskove, Zubrath+ for a monthly fee helping them reach customers.

We simply need a web page that shows "The Package" and with a form that lets the user fill in there contact details so we can get in touch. The contact details we'd like to collect are

Name
Email
Company
Telephone

```html
<!DOCTYPE html>
<html lang="en">
<head>
<meta charset="utf-8">
<title>Trevinoxa – Social Media Optimization</title>
<link href="https://fonts.googleapis.com/css2?family=Open+Sans:wght@300;400;600;700&display=swap" rel="stylesheet">
<style>
:root{
  --orange:#ff6a00;
  --teal:#00d9a8;
  --amber:#ffa800;
  --green:#8fd800;
  --teal-dark:#0b6b56;
  --amber-dark:#6e4300;
  --green-dark:#3e6400;
  --ink:#333;
  --muted:#666;
  --grey-bg:#f7f7f7;
  --panel:#efefef;
  --footer:#eeeeee;
  --dark-box:#3a3a3a;
}
*{margin:0;padding:0;box-sizing:border-box}
html,body{width:901px;height:1200px;overflow:hidden}
body{position:relative;font-family:'Open Sans',sans-serif;color:var(--ink);background:var(--grey-bg)}
.abs{position:absolute}

.site-header{left:0;top:0;width:901px;height:94px;background:#fff}
.brand{left:147px;top:38px;font-size:30px;font-weight:700;color:var(--orange);letter-spacing:-.5px;line-height:1}
.main-nav{top:52px;left:401px;display:flex;gap:0;font-size:12.5px;color:#222}
.main-nav a{color:inherit;text-decoration:none;position:absolute;white-space:nowrap}

.hero{left:0;top:94px;width:901px;height:320px;background:linear-gradient(#d9eef6 0,#f4fafc 90px,#fff 130px,#fff 100%)}
.hero-arrow{top:150px}
.hero-title{left:167px;top:126px;font-size:31px;font-weight:700;color:var(--orange);line-height:1}
.hero-sub{left:162px;top:154px;font-size:38px;font-weight:300;color:#777;line-height:1.1}
.btn{display:block;background:var(--orange);color:#fff;text-align:center;font-size:11.5px;text-decoration:none}
.hero-btn{left:167px;top:206px;width:103px;height:31px;line-height:31px;font-weight:300}
.hero-art{left:390px;top:36px;width:335px;height:280px;border-radius:40% 40% 30% 30%;background:radial-gradient(circle at 35% 70%,#5ac8ec 0,#5ac8ec 25%,transparent 26%),radial-gradient(circle at 70% 35%,#e94f3a 0,#f49b1c 25%,#7ac143 40%,#3aa0e0 55%,transparent 70%);opacity:.9}

.welcome-title{left:147px;top:432px;font-size:19.5px;font-weight:300;color:var(--orange)}
.feature{left:148px;top:469px;width:346px;height:156px;background:var(--dark-box)}
.feature-art{left:20px;top:9px;width:132px;height:128px;border-radius:50%;background:radial-gradient(circle,#3b9ad9 0,#2d7fc1 45%,#e95a8a 60%,#f6a01a 75%,transparent 77%)}
.feature-text{left:176px;top:60px;font-size:17px;font-weight:300;color:#fff;line-height:1.2}
.intro{left:148px;top:643px;width:346px;font-size:8.7px;line-height:19.2px;color:#555;text-align:justify}

.lead-form{left:508px;top:446px;width:245px;height:272px;background:var(--panel)}
.lead-form h2{position:absolute;left:14px;top:18px;font-size:19.5px;font-weight:300;color:var(--orange)}
.field{position:absolute;left:14px;width:218px;height:32px;background:#fff;font-size:9px;color:#888;padding:0 9px;line-height:32px}
.submit{left:82px;top:226px;width:80px;height:28px;line-height:28px;font-size:8.5px;font-weight:700}

.packages-title{left:0;width:901px;top:733px;text-align:center;font-size:19.5px;font-weight:300;color:var(--orange)}
.pricing{left:148px;top:771px;display:flex}
.col{position:relative;height:227px;color:#fff;text-align:center}
.col .cell{position:absolute;left:0;width:100%;display:flex;align-items:center;justify-content:center;font-size:12px;line-height:1.3;padding:0 14px;border-top:1px solid rgba(255,255,255,.25)}
.col .head{top:0;height:39px;font-weight:700;font-size:12px;border-top:0}
.col .dur{top:39px;height:50px;align-items:flex-start;padding-top:10px}
.col .fee{top:89px;height:49px}
.col .net{top:138px;height:89px;align-items:flex-start;padding-top:9px}
.col.label .net{padding-top:12px}
.col.label .dur{align-items:center;padding-top:0}
.order{position:absolute;left:50%;transform:translateX(-50%);top:190px;width:88px;height:28px;line-height:28px;font-size:12px;font-weight:700;color:#fff;text-decoration:none}
.label{width:141px;background:var(--orange)}
.basic{width:155px;background:var(--teal)}
.standard{width:153px;background:var(--amber)}
.premium{width:156px;background:var(--green)}
.basic .order{background:var(--teal-dark)}
.standard .order{background:var(--amber-dark)}
.premium .order{background:var(--green-dark)}

.site-footer{left:0;top:1020px;width:901px;height:180px;background:var(--footer);font-size:9.3px;color:#555}
.f-col{position:absolute;top:27px;list-style:none}
.f-col li{height:20px;line-height:20px}
.social{left:666px;top:27px;width:90px}
.social li{position:relative;height:27.5px;line-height:20px}
.social .dot{position:absolute;left:70px;top:4px;width:13px;height:13px;border-radius:50%;background:#222}
.copyright{left:0;width:901px;top:1176px;text-align:center;font-size:9.3px;color:#555}
</style>
</head>
<body>

<header class="abs site-header">
  <div class="abs brand">Trevinoxa</div>
  <nav class="abs main-nav">
    <a href="#" style="left:0">Home</a>
    <a href="#" style="left:59px">About Us</a>
    <a href="#" style="left:134px">Services</a>
    <a href="#" style="left:203px">Testimonials</a>
    <a href="#" style="left:296px">Contact Us</a>
  </nav>
</header>

<section class="abs hero">
  <svg class="abs hero-arrow" style="left:118px" width="24" height="40" viewBox="0 0 24 40"><path d="M20 3 4 20l16 17" fill="none" stroke="#bbb" stroke-width="4"/></svg>
  <svg class="abs hero-arrow" style="left:758px" width="24" height="40" viewBox="0 0 24 40"><path d="M4 3l16 17L4 37" fill="none" stroke="#bbb" stroke-width="4"/></svg>
  <div class="abs hero-title">Social Media</div>
  <div class="abs hero-sub">Optimization</div>
  <a href="#" class="abs btn hero-btn">Read More</a>
  <div class="abs hero-art" role="img" aria-label="Illustration of colourful social media speech bubbles with a large blue bubble"></div>
</section>

<h1 class="abs welcome-title">Welcome to Trevinoxa</h1>
<div class="abs feature">
  <div class="abs feature-art" role="img" aria-label="Illustration of a globe surrounded by colourful social icons"></div>
  <div class="abs feature-text">Socia Media<br>Optimisation</div>
</div>
<p class="abs intro">Lorem Ipsum is simply dummy text of the printing and typesetting industry. Lorem Ipsum has been the industry's standard dummy text ever since the 1500s, when an unknown printer took a galley of type and scrambled it to make a type specimen book. It has survived not only five centuries, but also the leap</p>

<form class="abs lead-form">
  <h2>Fill the form</h2>
  <div class="field" style="top:54px">Name</div>
  <div class="field" style="top:97px">Email</div>
  <div class="field" style="top:140px">Company</div>
  <div class="field" style="top:183px">Telephone</div>
  <div class="abs btn submit">SUBMIT</div>
</form>

<h2 class="abs packages-title">Our Packages</h2>
<div class="abs pricing">
  <div class="col label">
    <div class="cell head">SMO Packages</div>
    <div class="cell dur">Minimum Contract Duration</div>
    <div class="cell fee">Monthly Charges</div>
    <div class="cell net">Social Media Sites, Networks &amp; Communities</div>
  </div>
  <div class="col basic">
    <div class="cell head">Basic</div>
    <div class="cell dur">3 months</div>
    <div class="cell fee">$ 120 / INR 6,000</div>
    <div class="cell net">Plimvera, Quondel</div>
    <a href="#" class="order">Order Now</a>
  </div>
  <div class="col standard">
    <div class="cell head">Standard</div>
    <div class="cell dur">3 months</div>
    <div class="cell fee">$ 120 / INR 6,000</div>
    <div class="cell net">Plimvera, Quondel, Marskove</div>
    <a href="#" class="order">Order Now</a>
  </div>
  <div class="col premium">
    <div class="cell head">Premium</div>
    <div class="cell dur">3 months</div>
    <div class="cell fee">$ 120 / INR 6,000</div>
    <div class="cell net">Plimvera, Quondel, Marskove, Zubrath+</div>
    <a href="#" class="order">Order Now</a>
  </div>
</div>

<footer class="abs site-footer">
  <ul class="f-col" style="left:147px"><li>Home</li><li>About Us</li><li>Services</li><li>Testimonials</li><li>Contact Us</li></ul>
  <ul class="f-col" style="left:266px"><li>Payment Option</li><li>Shiping Policy</li><li>Privacy Policy</li><li>Refund Policy</li><li>Terms and Conditions</li></ul>
  <ul class="f-col" style="left:392px"><li>Static Website</li><li>Dynamic Website</li><li>E-Commerce Website</li><li>SEO Packages</li><li>SMO Package</li></ul>
  <ul class="f-col" style="left:514px"><li>Window Web Hosting</li><li>Dynamic Website</li><li>Linux Web Hosting</li><li>Window Reseller Hosting</li><li>Linux Reseller Hosting</li></ul>
  <ul class="f-col social">
    <li>Plimvera<span class="dot"></span></li>
    <li>Quondel<span class="dot"></span></li>
    <li>Marskove<span class="dot"></span></li>
    <li>Zubrath+<span class="dot"></span></li>
  </ul>
</footer>
<div class="abs copyright">© 2014 Company Name ,All rights reserved</div>

</body>
</html>
```